Animal Eye Clinic needs a Business card

We are a new veterinary ophthalmology practice (Tessaly Animal Eye Care) and we need a business card designed. We only see animal eyes - we are not a regular veterinary clinic. We already have a logo. We are looking for a professional, good looking business card to hand out to our clients. We are looking for something simple but professional and contemporary. Our logo is likely the only picture/graphic that needs to be on the card.
Updates

Contact Information for Business Card

Marisol Dunkley, BSc, DVM, MSc, DipACVO
Veterinary Ophthalmologist

Phone: 250.418.3097
Email: tessalyanimaleyecare@mailbrook.net
Website: tessalyanimaleyecare.net
Address: 1840 Pellworth Rd
Kelowna, BC, V4T 8M3

Colors

Designer to choose colors to be used in the design.

Requirements
Must have
• Our logo (attached)

```html
<!DOCTYPE html>
<html lang="en">
<head>
<meta charset="utf-8">
<title>Tessaly Animal Eye Care – Business Card</title>
<link rel="stylesheet" href="https://fonts.googleapis.com/css2?family=Josefin+Sans:wght@600;700&family=Montserrat:wght@600&display=swap">
<style>
  :root {
    --bg: #003420;
    --card-back: #042805;
    --teal: #0397a8;
    --grey: #808080;
    --leaf-dark: #033a12;
    --leaf-mid: #0a4a1a;
    --leaf-light: #3f6b1c;
  }
  * { margin: 0; padding: 0; box-sizing: border-box; }
  html, body { width: 1200px; height: 1200px; overflow: hidden; background: var(--bg); }
  .canvas { position: relative; width: 1200px; height: 1200px; }

  .card { position: absolute; width: 711px; height: 406px; box-shadow: 3px 3px 0 #000; overflow: hidden; }

  .card-front { left: 221px; top: 117px; }
  .front-pattern {
    position: absolute; inset: 0;
    background:
      radial-gradient(ellipse at 75% 40%, rgba(90,120,20,.55), transparent 45%),
      radial-gradient(ellipse at 20% 75%, rgba(70,110,25,.45), transparent 40%),
      linear-gradient(160deg, var(--leaf-mid), var(--leaf-dark) 55%, var(--leaf-light));
  }
  .brand {
    position: absolute; left: 0; right: 0; top: 178px;
    display: flex; justify-content: center; align-items: center; gap: 12px;
  }
  .brand-dot { width: 30px; height: 30px; border-radius: 50%; background: var(--teal); }
  .brand-name {
    font-family: "Montserrat", sans-serif; font-weight: 600;
    font-size: 22px; letter-spacing: 1.5px; text-transform: uppercase; color: var(--teal);
  }

  .card-back { left: 227px; top: 600px; background: var(--card-back); }
  .person { position: absolute; left: 40px; top: 42px; font-family: "Josefin Sans", sans-serif; font-weight: 700; text-transform: uppercase; line-height: 1; }
  .person-name { font-size: 25px; color: var(--teal); }
  .person-role { font-size: 25px; color: var(--grey); margin-top: 3px; }

  .band { position: absolute; left: 0; width: 681px; height: 28px; background: var(--teal);
    clip-path: polygon(0 0, 100% 0, 96.3% 100%, 0 100%); }
  .band-top { top: 105px; }
  .band-bottom { top: 358px; }

  .write-line { position: absolute; left: 0; width: 357px; height: 2px; background: var(--teal); }

  .contact { position: absolute; left: 373px; right: 24px; display: flex; align-items: center; gap: 12px;
    font-family: "Josefin Sans", sans-serif; font-weight: 600; font-size: 12px;
    letter-spacing: 1px; text-transform: uppercase; color: var(--teal); line-height: 1.15;
    white-space: nowrap; }
  .contact svg { width: 34px; height: 34px; flex: none; }
  .contact-email { font-size: 10.5px; letter-spacing: .5px; }
</style>
</head>
<body>
<div class="canvas">

  <section class="card card-front">
    <div class="front-pattern" role="img" aria-label="Green foliage-like striped camouflage pattern"></div>
    <div class="brand">
      <span class="brand-dot"></span>
      <span class="brand-name">Tessaly Animal Eye Care</span>
    </div>
  </section>

  <section class="card card-back">
    <div class="person">
      <p class="person-name">Marisol Dunkley, BSc, DVM, MSc, DipACVO</p>
      <p class="person-role">Veterinary Ophthalmologist</p>
    </div>

    <div class="band band-top"></div>

    <div class="write-line" style="top:173px"></div>
    <div class="write-line" style="top:225px"></div>
    <div class="write-line" style="top:273px"></div>
    <div class="write-line" style="top:321px"></div>

    <div class="contact" style="top:156px">
      <svg viewBox="0 0 34 34"><path d="M17 2a11 11 0 0 0-11 11c0 8 11 19 11 19s11-11 11-19A11 11 0 0 0 17 2zm0 15a4.5 4.5 0 1 1 0-9 4.5 4.5 0 0 1 0 9z" fill="var(--grey)"/></svg>
      <span>1840 Pellworth Rd<br>Kelowna, BC, V4T 8M3</span>
    </div>

    <div class="contact" style="top:208px">
      <svg viewBox="0 0 34 34"><circle cx="17" cy="17" r="17" fill="var(--grey)"/><circle cx="17" cy="13" r="4.5" fill="var(--card-back)"/><path d="M9 24c0-5 4-7 8-7s8 2 8 7z" fill="var(--card-back)"/></svg>
      <span>250.418.3097</span>
    </div>

    <div class="contact contact-email" style="top:256px">
      <svg viewBox="0 0 34 34" fill="none" stroke="var(--grey)" stroke-width="2"><rect x="4" y="13" width="26" height="19" rx="2"/><path d="M4 14l13 10 13-10"/><rect x="9" y="2" width="16" height="14"/><circle cx="17" cy="9" r="3"/></svg>
      <span>tessalyanimaleyecare@mailbrook.net</span>
    </div>

    <div class="contact" style="top:304px">
      <svg viewBox="0 0 34 34" fill="none" stroke="var(--grey)" stroke-width="2"><circle cx="17" cy="17" r="15" fill="var(--grey)" fill-opacity=".25"/><ellipse cx="17" cy="17" rx="7" ry="15"/><path d="M2 17h30M4 10h26M4 24h26M17 2v30"/></svg>
      <span>tessalyanimaleyecare.net</span>
    </div>

    <div class="band band-bottom"></div>
  </section>

</div>
</body>
</html>
```